STAFFONLYを変更
カメラをよりシンプルに
サイズの相談
ベースはこちらに決定いたします
ありがとうございます。
みなさまありがとうございます
最後まで悩みましたが
よりシンプルなもので
非関係者の抑制効果が一番ありそうなものを採用いたしました
関係者以外立ち入り禁止 POP POPデザインの仕事の依頼
LumivexCloudを中心にクラウドサービスを使った業務用アプリケーション開発をメインに行っております。
C#によるASP.NETによるWeb開発が中心で、WPFデスクトップアプリ、Formアプリ、Xamarinモバイルアプリを採用しております。
ハタラクモリでは上記プログラミングのパートナーを主に募集しています。
■募集に応募される方へのお願い
継続したお取引が可能な方を探しております。
フリーランス(一人法人含む)の方か、副業の方へご発注することが多いです。チームや法人、オフショアフロントの方と経験上成功したことがないです。
メッセージ中心のため、意図が伝わらず、容易に音信不通になります。実際に会うこともなくシステム上契約不履行時の違約金もないため、仕方がないことと割り切っていますが、大勢の方とのやり取りをしてメンバー選定しているので悲しくなります。逆にこちらからのレスが滞りご迷惑をおかけることもあります。
またプロトタイプで進めている関係で、要求がアバウトになることがほとんど。指示が二転三転することも。そういったことに神経質でない方がよいです。
トラブルで多いのが、資源を渡した瞬間に音信不通になる、成果物なしで支払いを余儀なくされる、生産的なやり取りではなく感情的なメッセージが来る、などです。こちらの作業内容や指示方法にも問題があることがありますので、初回の方は一定期間小規模予算でお互いが問題ないことを確認いただいてから継続契約します。
時々Skypeなどの打ち合わせを前提とされる方がおりますが、クラウドソーシングの特性を生かすとできるだけ時間を合わせて行うことが少ないほうが生産的で、必要最低限とさせて頂けますと幸いです。逆に作業時間帯はお好きな時間、何曜日でも構いません。フリーランスの方には十分な稼働時間を期待する半面、副業やフルで作業できないけど優れた技術者の開発リソースを安価に得られることがクラウドソーシングの最大のメリットだと考えています。
最後に、同じ自己紹介文で多くの仕事に同じメッセージで応募される方が多数おります。募集要項読んでいただけてない方は辞退しています。
いろいろ書いて申し訳ありませんが、私の考えに賛同してくださる方、ぜひ一緒に仕事させてください!
クライアント目線で柔軟な対応が可能な方と楽しく一緒に仕事をしたいです!

```html
<!DOCTYPE html>
<html lang="ja">
<head>
<meta charset="utf-8">
<title>Members Only Sign</title>
<link rel="stylesheet" href="https://fonts.googleapis.com/css2?family=Montserrat:wght@800&family=Noto+Sans+JP:wght@900&display=swap">
<style>
  :root {
    --ink: #111111;
    --paper: #ffffff;
  }
  html, body {
    margin: 0;
    padding: 0;
    overflow: hidden;
    background: var(--paper);
  }
  .sign {
    width: 1200px;
    height: 400px;
    display: block;
    background: var(--paper);
  }
  .sign__title {
    font-family: "Montserrat", "Arial Black", sans-serif;
    font-weight: 800;
    font-size: 112px;
    fill: var(--ink);
  }
  .sign__notice {
    font-family: "Noto Sans JP", sans-serif;
    font-weight: 900;
    font-size: 46px;
    fill: var(--ink);
  }
  .sign__rule {
    fill: var(--ink);
  }
  .sign__camera {
    fill: var(--ink);
  }
</style>
</head>
<body>
<svg class="sign" viewBox="0 0 1200 400" xmlns="http://www.w3.org/2000/svg">
  <text class="sign__title" x="70" y="218" textLength="622" lengthAdjust="spacingAndGlyphs">MENBERS</text>
  <text class="sign__title" x="788" y="218" textLength="352" lengthAdjust="spacingAndGlyphs">ONLY</text>
  <rect class="sign__rule" x="44" y="222" width="1116" height="4"/>
  <path class="sign__camera" role="img" aria-label="Security camera dome" d="M70 226 H250 V262 C250 310 210 342 160 342 C110 342 70 310 70 262 Z"/>
  <text class="sign__notice" x="642" y="290" textLength="488" lengthAdjust="spacingAndGlyphs">関係者以外立入禁止</text>
</svg>
</body>
</html>
```